Training program workbook Cover & Insert

We need a cover for a training manual for a Management and leadership program & the first topic title page.

We are an executive consultation business that develops training programs and provides in-house strategic support for businesses across different sectors. We see this will be an ongoing design project as we will be creating a cover for the folder (to be inserted into the A4 binder) and then as we develop the sections a series of title pages for each topic.
We are currently looking for designs for the Main cover and first topic ( 2 x A4 pages / like a double sided flyer really). The designs should reflect
- sophistication
- growth
- drive
- fun
- agility
With a theme that can be replicated across a series of topics e.g. communication, time effectiveness, conflict resolution etc etc

The Program is called "PLUME".
The tagline for the binder cover is
"Creating Leadership Agility in a Changing World"

The first topic is "TIME"
Tagline
Living & Working in "REAL" Time

We are open to any colour other than orange.

Target Market(s)

Training Program participants

Industry/Entity Type

Training

Font styles to use
Serif

Colors

Designer to choose colors to be used in the design.

Requirements
Must have
• A design framework that can be expanded for various topic cover pages within the manual.
• Eye Catching graphics that excite the viewer and entice them to continue reading
Nice to have
• Copyright (symbol) Verrick Group in small font at the bottom of the page
Should not have
• Typical daggy old school training images

```html
<!DOCTYPE html>
<html lang="en">
<head>
<meta charset="utf-8">
<title>PLUME Workbook – Cover &amp; Topic Page</title>
<link rel="stylesheet" href="https://fonts.googleapis.com/css2?family=Roboto:wght@400;900&display=swap">
<style>
  :root {
    --backdrop: #aba6a2;
    --paper: #f7f7f5;
    --paper-shade: #ecebe8;
    --gold: #c4975a;
    --gold-light: #e6c48e;
    --gold-dark: #a5773f;
    --sky-top: #8fa6c4;
    --sky-mid: #b7c6d9;
    --sky-low: #a9bcd3;
    --city-dark: #3a3a40;
    --city-warm: #8a7258;
    --city-glow: #c9a878;
    --ink: #141414;
    --white: #ffffff;
  }
  * { box-sizing: border-box; margin: 0; padding: 0; }
  html, body {
    width: 1200px; height: 833px; overflow: hidden;
    background: var(--backdrop);
    font-family: "Roboto", Arial, sans-serif;
  }
  .spread {
    position: absolute; left: 63px; top: 36px;
    width: 1074px; height: 760px;
    display: flex;
    box-shadow: 0 10px 30px rgba(0,0,0,0.25);
  }
  .page {
    position: relative; width: 537px; height: 760px;
    background: linear-gradient(180deg, var(--paper), var(--paper-shade));
    overflow: hidden;
  }
  .page__visual {
    position: absolute; left: 0; top: 0; width: 100%; height: 548px;
  }
  .visual--sky {
    background: linear-gradient(180deg, var(--sky-top) 0%, var(--sky-mid) 55%, var(--sky-low) 100%);
  }
  .visual--city {
    background:
      radial-gradient(ellipse 70% 25% at 50% 32%, rgba(230,170,100,0.55), transparent 70%),
      linear-gradient(180deg, var(--city-dark) 0%, #4d4644 35%, var(--city-warm) 70%, var(--city-glow) 100%);
  }
  .page__rule {
    position: absolute; left: 0; width: 100%; top: 548px; height: 12px;
    border-top: 4px solid var(--gold);
    border-bottom: 2px solid var(--gold);
    background: var(--paper);
  }
  .cover__frame {
    position: absolute; left: 24px; top: 22px; right: 24px; height: 470px;
    border: 3px solid var(--gold);
  }
  .cover__skydivers {
    position: absolute; left: 70px; top: 28px; width: 395px; height: 330px;
    border-radius: 50%;
    background: radial-gradient(circle, rgba(70,70,80,0.55) 0%, rgba(90,90,100,0.35) 55%, transparent 72%);
  }
  .section-title {
    position: absolute; left: 0; width: 100%;
    text-align: center; font-weight: 900; letter-spacing: 1px;
  }
  .section-title--gold {
    top: 375px; font-size: 56px;
    background: linear-gradient(180deg, var(--gold-light) 0%, var(--gold) 55%, var(--gold-dark) 100%);
    -webkit-background-clip: text; background-clip: text; color: transparent;
  }
  .section-title--white {
    top: 375px; font-size: 56px; color: var(--white);
  }
  .topic__icon {
    position: absolute; left: 50%; top: 250px; width: 100px; height: 110px;
    transform: translateX(-50%);
  }
  .tagline {
    position: absolute; left: 0; width: 100%; top: 600px;
    text-align: center; color: var(--ink); line-height: 1.2;
  }
  .tagline__lead { font-weight: 900; font-size: 29px; display: block; }
  .tagline__sub { font-weight: 400; font-size: 29px; display: block; }
</style>
</head>
<body>
  <main class="spread">
    <section class="page page--cover">
      <div class="page__visual visual--sky" role="img" aria-label="Formation of skydivers holding hands in a spiral against a blue sky"></div>
      <div class="cover__frame">
        <div class="cover__skydivers" role="img" aria-label="Skydiver formation"></div>
        <h1 class="section-title section-title--gold">PLUME</h1>
      </div>
      <div class="page__rule"></div>
      <p class="tagline">
        <span class="tagline__lead">Creating Leadership Agility</span>
        <span class="tagline__sub">in a Changing World</span>
      </p>
    </section>

    <section class="page page--topic">
      <div class="page__visual visual--city" role="img" aria-label="City street at night with streaking light trails and office buildings"></div>
      <svg class="topic__icon" viewBox="0 0 100 110" aria-hidden="true">
        <g fill="none" stroke="#ffffff" stroke-width="9" stroke-linecap="round" stroke-linejoin="round">
          <line x1="8" y1="8" x2="92" y2="8"/>
          <line x1="8" y1="102" x2="92" y2="102"/>
          <path d="M22 8 C22 40 50 42 50 55 C50 68 22 70 22 102"/>
          <path d="M78 8 C78 40 50 42 50 55 C50 68 78 70 78 102"/>
        </g>
        <path d="M36 30 L64 30 L50 48 Z M30 96 L50 76 L70 96 Z" fill="#ffffff"/>
      </svg>
      <h2 class="section-title section-title--white">TIME</h2>
      <div class="page__rule"></div>
      <p class="tagline">
        <span class="tagline__lead">Living &amp; Working</span>
        <span class="tagline__sub">in “REAL” Time</span>
      </p>
    </section>
  </main>
</body>
</html>
```